Tales from Kin Logo Design plus business cards design

We are a start up company that will help seniors write their memoirs...beginning with a few ancestors and their heritage and continuing through their own history...how they would like to be remembered in the next generation. I envision a card with a senior citizen at an older writing desk, writing her memoirs, with a book (maybe standing on top, leaning slightly) that has the words Tales from Kin.com on the back binding. OR maybe a senior couple walking into the sunset with the same book somewhere in the frame. Communicating the relevance of every life being significant to those that come after them...when a genealogy doesn't say enough about the details of ones life. Please note that I am open to the professionals own ideas...I am not locked into my concepts. On the back of the card I would like one or two phrases..."A Genealogy Doesn't Say Enough" and/or "Every life legacy is uniquely significant to the next generation".
Updates

I have added a couple of photos for ideas that may be used if needed.

I have both increased and committed the payment! Thanks for the reminder!

Reason: We increased the payment commitment and added some photo ideas to help.

We want to thank EVERYONE who participated in this contest. There were so many wonderful and VERY professional proposals...making it very challenging to decide on one! We are posting a new contest for a brochure now and hope many of you will participate. May God bless your endeavors.

Target Market(s)

Senior populous & baby boomer generation.

Industry/Entity Type

Business

Logo Text

Tales from Kin ordinary lives...extraordinary legacy

Requirements
Must have
• Relevant info:
Domain name: talesfromkin.com
email: info@talesfromkin.com
phone: 1-855-GAB-TALE toll free
1-717-382-5619 local
name: Doris Whitlock, M.A.
Nice to have
• photo of senior or senior couple....book with our web address on the binding. I attached two photos that could work if cropped and enhanced. Words need to be deleted from the one photo of senior at a writing desk and couple on the beach could use a sunset sky and other people cropped out. Just ideas...don't know if you have better ones or prefer a different idea.

```html
<!DOCTYPE html>
<html lang="en">
<head>
<meta charset="utf-8">
<title>Tales from Kin – Business Card</title>
<link rel="stylesheet" href="https://fonts.googleapis.com/css2?family=Noto+Sans:wght@400;700&display=swap">
<style>
  :root {
    --card-cream: #f2f0d6;
    --ink: #0d0d0d;
  }
  html, body {
    margin: 0;
    padding: 0;
    width: 749px;
    height: 1200px;
    overflow: hidden;
    background: var(--card-cream);
  }
  .card {
    position: relative;
    width: 749px;
    height: 1200px;
    background: var(--card-cream);
    color: var(--ink);
    font-family: "Noto Sans", sans-serif;
  }
  .brand {
    position: absolute;
    left: 0;
    top: 222px;
    width: 749px;
    text-align: center;
    font-size: 56px;
    font-weight: 400;
    line-height: 1.2;
    margin: 0;
    color: var(--ink);
  }
  .holder {
    position: absolute;
    left: 90px;
    top: 693px;
    margin: 0;
    font-size: 54px;
    font-weight: 700;
    line-height: 1.2;
    white-space: nowrap;
  }
  .contact-row {
    position: absolute;
    left: 0;
    width: 749px;
  }
  .contact-icon {
    position: absolute;
  }
  .contact-text {
    position: absolute;
    left: 164px;
    margin: 0;
    font-size: 39px;
    line-height: 46px;
    white-space: nowrap;
  }
  .contact-note {
    font-size: 28px;
  }
  .phone-row { top: 807px; }
  .phone-row .contact-icon { left: 81px; top: 13px; }
  .email-row { top: 965px; }
  .email-row .contact-icon { left: 95px; top: -16px; }
  .email-row .contact-text { left: 174px; }
  .web-row { top: 1069px; }
  .web-row .contact-icon { left: 90px; top: -13px; }
  .web-row .contact-text { left: 174px; }
</style>
</head>
<body>
<main class="card">
  <h1 class="brand">Tales from Kin.com</h1>

  <h2 class="holder">Doris Whitlock, M.A.</h2>

  <section class="contact-row phone-row">
    <svg class="contact-icon" width="65" height="62" viewBox="0 0 65 62" aria-hidden="true">
      <path d="M14 2 L24 16 Q26 20 22 23 L18 26 Q24 38 38 45 L41 41 Q44 38 48 40 L62 49 Q65 52 61 56 L56 60 Q50 63 40 58 Q18 47 5 24 Q0 13 3 8 L8 3 Q11 0 14 2 Z" fill="var(--ink)"/>
    </svg>
    <p class="contact-text">1-717-382-5619 <span class="contact-note">(local)</span><br>1-855-GAB-TALE <span class="contact-note">(toll free)</span></p>
  </section>

  <section class="contact-row email-row">
    <svg class="contact-icon" width="60" height="52" viewBox="0 0 60 52" aria-hidden="true">
      <path d="M2 20 L30 2 L58 20 Z" fill="var(--ink)"/>
      <text x="30" y="17" text-anchor="middle" font-family="Noto Sans, sans-serif" font-size="12" font-weight="700" fill="var(--card-cream)">@</text>
      <rect x="2" y="20" width="56" height="30" fill="var(--card-cream)" stroke="var(--ink)" stroke-width="3"/>
      <path d="M2 20 L30 38 L58 20 M2 50 L24 34 M58 50 L36 34" fill="none" stroke="var(--ink)" stroke-width="3"/>
    </svg>
    <p class="contact-text">info@talesfromkin.com</p>
  </section>

  <section class="contact-row web-row">
    <svg class="contact-icon" width="64" height="64" viewBox="0 0 64 64" aria-hidden="true">
      <circle cx="32" cy="32" r="29" fill="none" stroke="var(--ink)" stroke-width="5"/>
      <ellipse cx="32" cy="32" rx="12" ry="29" fill="none" stroke="var(--ink)" stroke-width="3"/>
      <path d="M5 32 H59 M10 18 H54 M10 46 H54" fill="none" stroke="var(--ink)" stroke-width="3"/>
    </svg>
    <p class="contact-text">www.talesfromkin.com</p>
  </section>
</main>
</body>
</html>
```